Etikett für Weißwein vom Gardasee
Guten Tag liebe BlauFeder77, herzlichen Dank für die schnelle und professionelle Zusendung der Print-Dateien. Die gesamte Abwicklung war top! Wir freuen uns auf unser neues Custoza Etikett. :-) Mit besten Grüßen Petra Holm
Zielgruppe
Groß- und Einzelhandel für Wein
Aufgabenstellung
Es handelt sich um ein Etikett für einen Weißwein vom Gardasee.
Es gibt bereits ein eigenes Etikett. (siehe Upload)
Wichtig ist das 'VL' im Etikette als Logo beizubehalten oder weiter zu entwickeln. (Siehe Upload)
Ansonsten gerne Elemente, die auf den Gardasee hinweisen (emotional sehr positiv belegt)
Anbei Flaschenfoto mit Flaschenfarbe und Farbe der Kapsel - die Farben des Etiketts sollten dazu passen

```html
<!DOCTYPE html>
<html lang="it">
<head>
<meta charset="utf-8">
<title>Custoza – Etikett</title>
<link rel="stylesheet" href="https://fonts.googleapis.com/css2?family=EB+Garamond:wght@400&display=swap">
<style>
  :root {
    --page-bg: #ffffff;
    --label-bg: #d0d2e3;
    --mark-blue: #5a7499;
    --name-grey: #5a5355;
    --subline-mauve: #8a7f85;
  }
  html, body {
    margin: 0;
    padding: 0;
    width: 1200px;
    height: 3600px;
    overflow: hidden;
    background: var(--page-bg);
  }
  .canvas {
    position: relative;
    width: 1200px;
    height: 3600px;
  }
  .wine-label {
    position: absolute;
    left: 100px;
    top: 1026px;
    width: 1000px;
    height: 1548px;
    background: var(--label-bg);
    font-family: "EB Garamond", "Times New Roman", serif;
  }
  .brand-mark {
    position: absolute;
    left: 0;
    right: 0;
    top: 500px;
    text-align: center;
    font-size: 400px;
    font-weight: 400;
    line-height: 1;
    color: var(--mark-blue);
    letter-spacing: 4px;
  }
  .wine-name {
    position: absolute;
    left: 0;
    width: 920px;
    top: 1140px;
    margin: 0;
    text-align: center;
    font-size: 88px;
    font-weight: 400;
    line-height: 1;
    letter-spacing: 2px;
    color: var(--name-grey);
  }
  .appellation {
    position: absolute;
    left: 0;
    right: 0;
    top: 1290px;
    margin: 0;
    text-align: center;
    font-size: 46px;
    font-weight: 400;
    line-height: 1;
    word-spacing: 10px;
    color: var(--subline-mauve);
  }
</style>
</head>
<body>
  <main class="canvas">
    <section class="wine-label">
      <div class="brand-mark">VL</div>
      <h1 class="wine-name">CUSTOZA</h1>
      <p class="appellation">denominazione di rigine controllata</p>
    </section>
  </main>
</body>
</html>
```